Website for a new investor-focused estate agency portal

Require a website for a new investor-focused estate agency portal, this will interface with our exisitng API for data posting and retrieval. We have a logo for the business, but will happily change the colour palette to suit the design.
Requirements:
1) Landing page to describe the business
- Feature line showing the latest properties in our listings
- Announcement section (e.g. mobile app coming soon)
- Text area - what we do for Investors
- Text area - what we do for Agents and sourcers
- Text area - what we do for Home buyers
- Small Q&A
- Subscription pricing description and sign up
2) Content page (product updates page)
A timeline to list list releases, new features and other improvements to the service, website and app, shown in most recent date order.
3) A property search/result page including search form
4) A single property detail page, including
- carousel for images and video
- map
- text content
5) A data entry page to enter property data into the system. This page will contain a sidebar menu, property name, address, description, and about 10 other fields (detail to be provided). The attached screen dump files are snapshot of the wireframe form used by the development team for the property entry page.
Target Market(s)
Property investors / Real estate buyer's including personal home buyers.
Number of Pages Required
5+ page
Colors
Designer to choose colors to be used in the design.
Requirements
Must have
- Clean, crisp design and presentaion.
Nice to have
- The Search/result page (3) and the detail page (4) may have 2-3 elements for paid advertising but should also look good without those elements.
Should not have
- Must not be too busy with distracting elements

```html
<!DOCTYPE html>
<html lang="en">
<head>
<meta charset="utf-8">
<title>Keystone Yield – Investment Property Portal</title>
<link href="https://fonts.googleapis.com/css2?family=Montserrat:wght@400;500;600;700&display=swap" rel="stylesheet">
<style>
:root{
  --brand:#342a72;
  --brand-deep:#2a2163;
  --brand-soft:#6c5fb0;
  --ink:#222;
  --muted:#888;
  --line:#e6e6ea;
  --panel:#f3f3f5;
  --field:#ececee;
  --white:#fff;
  --black:#0d0d0d;
}
*{margin:0;padding:0;box-sizing:border-box}
html,body{width:1200px;height:3158px;overflow:hidden}
body{position:relative;font-family:'Montserrat',sans-serif;color:var(--ink);background:var(--white)}
.abs{position:absolute}
a{color:inherit;text-decoration:none}

/* header */
.topbar{left:0;top:0;width:1200px;height:75px;border-bottom:1px solid var(--line)}
.brand{left:164px;top:15px;display:flex;align-items:center;gap:14px}
.brand-mark{width:40px;height:40px;border:2px solid var(--brand)}
.brand-name{font-weight:600;font-size:15px;color:var(--brand);letter-spacing:.3px}
.contact-item{top:34px;font-size:11px;color:#555;display:flex;align-items:center;gap:10px;white-space:nowrap}
.signup{left:911px;top:28px;width:127px;height:28px;background:var(--brand);color:#fff;font-size:10px;font-weight:700;display:flex;align-items:center;justify-content:center;border-radius:3px}
.nav{left:0;top:75px;width:1200px;height:61px;border-bottom:1px solid var(--line)}
.nav a{position:absolute;top:26px;font-size:11px;font-weight:500;color:#333}
.nav a.active{color:var(--brand);font-weight:600}

/* hero */
.hero{left:0;top:136px;width:1200px;height:417px;background:linear-gradient(160deg,#6e6aa6 0%,#4d4790 45%,#3a3180 100%)}
.hero-kicker{left:0;width:1200px;top:295px;text-align:center;color:#fff;font-weight:600;font-size:14px;letter-spacing:.3px}
.hero-title{left:0;width:1200px;top:316px;text-align:center;color:#fff;font-weight:700;font-size:39px}
.arrow{top:325px}

/* search */
.finder{left:0;top:553px;width:1200px;height:219px;background:var(--panel)}
.finder-title{left:163px;top:585px;font-size:15px;font-weight:600;color:var(--brand)}
.field{height:35px;background:var(--field);border:1px solid #dcdce0;border-radius:3px;font-size:11px;color:#777;display:flex;align-items:center;padding-left:16px}
.field .caret{position:absolute;right:14px;top:15px}
.btn-search{background:var(--brand);color:#fff;font-weight:600;border:none;justify-content:center;padding:0}
.more{left:778px;top:685px;font-size:11px;font-weight:600;color:#222}
.more span{display:flex;align-items:center;gap:10px;color:var(--brand);margin-top:6px}

/* listing */
.eyebrow{font-size:10px;color:#666;letter-spacing:.2px;font-weight:500}
.section-title{font-size:30px;font-weight:600;color:var(--brand)}
.card{top:939px;width:278px;height:315px;background:#fff;box-shadow:0 1px 4px rgba(0,0,0,.12)}
.card .photo{width:278px;height:141px;position:relative;overflow:hidden}
.card .ribbon{position:absolute;left:-36px;top:22px;width:150px;height:24px;background:var(--brand);color:#fff;font-size:12px;transform:rotate(-35deg);display:flex;align-items:center;justify-content:center}
.card .price{position:absolute;left:13px;top:154px;font-size:20px;font-weight:600;color:var(--brand)}
.card .price small{font-size:11px;color:#555;font-weight:500;margin-right:4px}
.card .name{position:absolute;left:13px;top:199px;font-size:14px;font-weight:500}
.card .loc{position:absolute;left:13px;top:224px;font-size:11px;color:#888;display:flex;gap:8px;align-items:center}
.card .specs{position:absolute;left:0;top:260px;width:278px;display:flex;justify-content:space-around;font-size:10px;color:#888;text-align:center}
.card .specs div{display:flex;flex-direction:column;align-items:center;gap:6px}

/* services */
.service{top:1392px;width:230px;text-align:center}
.service h4{font-size:12px;font-weight:700;margin-top:14px}
.service p{font-size:10px;line-height:19.5px;color:#666;margin-top:6px}

/* app band */
.app{left:0;top:1617px;width:1200px;height:265px;background:linear-gradient(90deg,#4a4180 0%,#5b5091 55%,#6a5f9d 100%)}
.app-title{left:160px;top:1716px;font-size:27px;font-weight:600;color:#fff}
.app-copy{left:160px;top:1763px;width:500px;font-size:12px;line-height:23px;color:#fff}
.band-clip{left:0;top:1540px;width:1200px;height:342px;overflow:hidden}
.device{left:930px;top:50px;width:260px;height:420px;border-radius:34px;background:linear-gradient(160deg,#f4f4f8,#cfcde0);transform:rotate(-22deg);transform-origin:top left}
.device-screen{position:absolute;left:18px;top:26px;right:18px;bottom:0;border-radius:20px 20px 0 0;background:linear-gradient(160deg,#5a4fa0,#3d3282)}

/* faq */
.faq-title{left:160px;top:2040px;font-size:24px}
.faq-text{left:161px;top:2080px;width:490px;font-size:11px;line-height:22.5px;color:#555}
.acc{left:162px;width:420px;height:16px;font-size:12px;font-weight:600}
.acc .dash{position:absolute;left:0;top:8px;width:17px;height:2px;background:var(--brand)}
.acc .q{position:absolute;left:33px;top:0}
.acc .chev{position:absolute;right:0;top:1px}
.acc-body{left:196px;top:2196px;width:380px;font-size:10.5px;line-height:19.5px;color:#888}
.office{left:686px;top:1970px;width:352px;height:417px;background:linear-gradient(150deg,#2a2a2c 0%,#4b4a4c 35%,#d6d3cc 65%,#f1efe9 100%)}

/* pricing */
.pricing{left:0;top:2482px;width:1200px;height:476px;background:var(--panel)}
.pricing-title{left:0;width:1200px;top:2528px;text-align:center;font-size:22px;font-weight:600;color:var(--brand)}
.plan{top:2610px;width:226px;height:262px;background:#fff}
.plan .head{position:absolute;left:0;top:0;width:198px;height:52px;color:#fff;background:var(--brand)}
.plan .tier{position:absolute;left:14px;top:10px;font-size:15px}
.plan .rate{position:absolute;right:18px;top:32px;font-size:15px}
.plan .rate small{font-size:11px}
.plan ul{list-style:none;position:absolute;top:80px;width:100%;text-align:center;font-size:11px;color:#888}
.plan li{height:30px}
.plan li b{color:var(--brand);font-weight:600}
.plan .sub{position:absolute;left:59px;top:232px;width:109px;height:30px;background:var(--brand);color:#fff;font-size:14px;display:flex;align-items:center;justify-content:center}
.plan.dark .head,.plan.dark .sub{background:var(--black)}

/* footer */
.footer{left:0;top:2958px;width:1200px;height:200px;background:linear-gradient(180deg,#3b3283,#2e2670);color:#fff}
.foot-head{top:2992px;color:#fff;font-size:13.5px;font-weight:600}
.foot-copy{left:156px;top:3030px;width:260px;font-size:9.5px;line-height:22px;color:#fff}
.flink{font-size:9.5px;color:#fff}
.social{top:3039px;width:18px;height:18px;border-radius:50%;background:#fff}
.copy{left:0;width:1200px;top:3128px;text-align:center;font-size:9px;color:#ddd}
</style>
</head>
<body>

<!-- header -->
<header class="abs topbar">
  <div class="abs brand"><span class="brand-mark"></span><span class="brand-name">KEYSTONE YIELD</span></div>
  <div class="abs contact-item" style="left:680px">
    <svg width="16" height="16" viewBox="0 0 24 24" fill="none" stroke="#555" stroke-width="1.5"><path d="M5 3h4l2 5-2.5 1.5a11 11 0 0 0 6 6L16 13l5 2v4a2 2 0 0 1-2 2A17 17 0 0 1 3 5a2 2 0 0 1 2-2z"/></svg>555-0148
  </div>
  <div class="abs contact-item" style="left:787px;top:33px">
    <svg width="18" height="16" viewBox="0 0 24 20" fill="none" stroke="#555" stroke-width="1.5"><rect x="2" y="6" width="20" height="13"/><path d="M2 6l10 7 10-7M6 6V2h12v4"/></svg>desk@kyield.co
  </div>
  <a class="abs signup">SIGN UP</a>
</header>
<nav class="abs nav">
  <a class="active" style="left:161px">Home</a>
  <a style="left:238px">About</a>
  <a style="left:318px">What We Do</a>
  <a style="left:433px">Pricing</a>
  <a style="left:519px">Listing</a>
  <a style="left:599px">Contact</a>
</nav>

<!-- hero -->
<section class="abs hero" role="img" aria-label="Modern white villa photographed from below under a purple tint"></section>
<div class="abs hero-kicker">BE READY TO DISCOVER</div>
<h1 class="abs hero-title">Your Best Investment Opportunity</h1>
<svg class="abs arrow" style="left:56px" width="18" height="30" viewBox="0 0 18 30"><path d="M15 2L3 15l12 13" fill="none" stroke="#fff" stroke-width="2"/></svg>
<svg class="abs arrow" style="left:1130px" width="18" height="30" viewBox="0 0 18 30"><path d="M3 2l12 13L3 28" fill="none" stroke="#fff" stroke-width="2"/></svg>

<!-- search -->
<section class="abs finder"></section>
<h3 class="abs finder-title">FIND YOUR PROPERTY</h3>
<div class="abs field" style="left:161px;top:623px;width:185px">Select Type<svg class="caret" width="8" height="5"><path d="M0 0h8L4 5z" fill="#777"/></svg></div>
<div class="abs field" style="left:366px;top:623px;width:184px">Select Location<svg class="caret" width="8" height="5"><path d="M0 0h8L4 5z" fill="#777"/></svg></div>
<div class="abs field" style="left:570px;top:623px;width:184px">Bedrooms<svg class="caret" width="8" height="5"><path d="M0 0h8L4 5z" fill="#777"/></svg></div>
<div class="abs field" style="left:773px;top:623px;width:184px">Bathrooms<svg class="caret" width="8" height="5"><path d="M0 0h8L4 5z" fill="#777"/></svg></div>
<div class="abs field" style="left:161px;top:681px;width:185px">Min Area (sqft)</div>
<div class="abs field" style="left:366px;top:681px;width:184px">Max Area (sqft)</div>
<div class="abs field btn-search" style="left:570px;top:681px;width:184px">Search Properties</div>
<div class="abs more">Need more search options?
  <span><svg width="13" height="13"><rect width="13" height="13" rx="2" fill="var(--brand)"/><path d="M6.5 3v7M3 6.5h7" stroke="#fff" stroke-width="1.6"/></svg>More Search Options</span>
</div>

<!-- recent listing -->
<div class="abs eyebrow" style="left:162px;top:850px">LATEST PROPERTIES</div>
<h2 class="abs section-title" style="left:160px;top:862px">Recent Listing</h2>

<article class="abs card" style="left:161px">
  <div class="photo" role="img" aria-label="Thatched-roof wooden house on a lawn" style="background:linear-gradient(180deg,#cfd9e4 0%,#8a7a66 45%,#3b3a38 75%,#6f8a4e 100%)"><div class="ribbon">Recent</div></div>
  <div class="price"><small>from</small>$250.000</div>
  <div class="name">Beautiful Wooden House</div>
  <div class="loc"><svg width="9" height="12" viewBox="0 0 9 12"><path d="M4.5 0A4.5 4.5 0 0 0 0 4.5C0 8 4.5 12 4.5 12S9 8 9 4.5A4.5 4.5 0 0 0 4.5 0z" fill="#999"/><circle cx="4.5" cy="4.5" r="1.6" fill="#fff"/></svg>House Location</div>
  <div class="specs">
    <div><svg width="14" height="10"><path d="M1 1v9M1 6h12v4M4 4h9v2" stroke="#999" fill="none" stroke-width="1.4"/></svg>3 Beds</div>
    <div><svg width="14" height="11"><path d="M1 5h12v3a2 2 0 0 1-2 2H3a2 2 0 0 1-2-2zM3 5V1h3" stroke="#999" fill="none" stroke-width="1.3"/></svg>3 Bathrooms</div>
    <div><svg width="13" height="13"><rect x="1" y="1" width="11" height="11" stroke="#999" fill="none"/><path d="M6.5 1v11M1 6.5h11" stroke="#999"/></svg>300 Sq ft</div>
    <div><svg width="14" height="14"><path d="M3 1h5v12H3zM8 9h5v4" stroke="#999" fill="none" stroke-width="1.3"/></svg>3 Rooms</div>
  </div>
</article>

<article class="abs card" style="left:461px">
  <div class="photo" role="img" aria-label="Modern house terrace overlooking the sea" style="background:linear-gradient(180deg,#e9eef2 0%,#b9c8d4 40%,#4f5a60 65%,#7e8a8e 100%)"><div class="ribbon">Recent</div></div>
  <div class="price"><small>from</small>$250.000</div>
  <div class="name">Beautiful House Near Sea</div>
  <div class="loc"><svg width="9" height="12" viewBox="0 0 9 12"><path d="M4.5 0A4.5 4.5 0 0 0 0 4.5C0 8 4.5 12 4.5 12S9 8 9 4.5A4.5 4.5 0 0 0 4.5 0z" fill="#999"/><circle cx="4.5" cy="4.5" r="1.6" fill="#fff"/></svg>House Location</div>
  <div class="specs">
    <div><svg width="14" height="10"><path d="M1 1v9M1 6h12v4M4 4h9v2" stroke="#999" fill="none" stroke-width="1.4"/></svg>3 Beds</div>
    <div><svg width="14" height="11"><path d="M1 5h12v3a2 2 0 0 1-2 2H3a2 2 0 0 1-2-2zM3 5V1h3" stroke="#999" fill="none" stroke-width="1.3"/></svg>3 Bathrooms</div>
    <div><svg width="13" height="13"><rect x="1" y="1" width="11" height="11" stroke="#999" fill="none"/><path d="M6.5 1v11M1 6.5h11" stroke="#999"/></svg>300 Sq ft</div>
    <div><svg width="14" height="14"><path d="M3 1h5v12H3zM8 9h5v4" stroke="#999" fill="none" stroke-width="1.3"/></svg>3 Rooms</div>
  </div>
</article>

<article class="abs card" style="left:760px">
  <div class="photo" role="img" aria-label="Red brick family house with white trim" style="background:linear-gradient(180deg,#dfe6ee 0%,#8c6a5c 40%,#9b4a3e 65%,#c9c4bb 100%)"><div class="ribbon">Recent</div></div>
  <div class="price"><small>from</small>$250.000</div>
  <div class="name">Red Wooden House</div>
  <div class="loc"><svg width="9" height="12" viewBox="0 0 9 12"><path d="M4.5 0A4.5 4.5 0 0 0 0 4.5C0 8 4.5 12 4.5 12S9 8 9 4.5A4.5 4.5 0 0 0 4.5 0z" fill="#999"/><circle cx="4.5" cy="4.5" r="1.6" fill="#fff"/></svg>House Location</div>
  <div class="specs">
    <div><svg width="14" height="10"><path d="M1 1v9M1 6h12v4M4 4h9v2" stroke="#999" fill="none" stroke-width="1.4"/></svg>3 Beds</div>
    <div><svg width="14" height="11"><path d="M1 5h12v3a2 2 0 0 1-2 2H3a2 2 0 0 1-2-2zM3 5V1h3" stroke="#999" fill="none" stroke-width="1.3"/></svg>3 Bathrooms</div>
    <div><svg width="13" height="13"><rect x="1" y="1" width="11" height="11" stroke="#999" fill="none"/><path d="M6.5 1v11M1 6.5h11" stroke="#999"/></svg>300 Sq ft</div>
    <div><svg width="14" height="14"><path d="M3 1h5v12H3zM8 9h5v4" stroke="#999" fill="none" stroke-width="1.3"/></svg>3 Rooms</div>
  </div>
</article>

<!-- what we do -->
<h2 class="abs section-title" style="left:0;width:1200px;text-align:center;top:1313px;font-size:27px">What We Do</h2>
<div class="abs service" style="left:185px">
  <svg width="36" height="34" viewBox="0 0 36 34" fill="none" stroke="var(--brand)" stroke-width="1.5"><path d="M2 12L18 2l16 10M5 12v20h26V12M9 18h8v8H9zM21 18h6v14"/></svg>
  <h4>For Investors</h4>
  <p>Lorem ipsum dolor sit amet, consectetur adipiscing elit, sed do eiusmod tempor incididunt ut labore et dolore magna aliqua.</p>
</div>
<div class="abs service" style="left:485px">
  <svg width="36" height="34" viewBox="0 0 36 34" fill="none" stroke="var(--brand)" stroke-width="1.5"><path d="M4 14L18 3l14 11M7 12v20h22V12M12 17h4v4h-4zM20 17h4v4h-4zM15 32v-7h6v7"/></svg>
  <h4>For Agents and Sourcers</h4>
  <p>Lorem ipsum dolor sit amet, consectetur adipiscing elit, sed do eiusmod tempor incididunt ut labore et dolore magna aliqua.</p>
</div>
<div class="abs service" style="left:783px">
  <svg width="36" height="34" viewBox="0 0 36 34" fill="none" stroke="var(--brand)" stroke-width="1.5"><path d="M3 13L18 2l15 11M6 11v21h24V11M14 32v-9h8v9M15 15h6"/></svg>
  <h4>For Home Buyers</h4>
  <p>Lorem ipsum dolor sit amet, consectetur adipiscing elit, sed do eiusmod tempor incididunt ut labore et dolore magna aliqua.</p>
</div>

<!-- app announcement -->
<section class="abs app" role="img" aria-label="Suburban houses under a purple overlay"></section>
<div class="abs band-clip">
  <div class="abs device" role="img" aria-label="Smartphone showing the app start screen"><div class="device-screen"></div></div>
</div>
<h2 class="abs app-title">Mobile App Coming Soon!</h2>
<p class="abs app-copy">Lorem ipsum dolor sit amet, consectetur adipiscing elit, sed do eiusmod tempor incididunt ut labore et dolore magna aliqua. Quis ipsum suspendisse ultrices</p>

<!-- faq -->
<div class="abs eyebrow" style="left:162px;top:2022px">FAQ</div>
<h2 class="abs section-title faq-title">Where Can We Help You?</h2>
<p class="abs faq-text">Lorem ipsum dolor sit amet, consectetur adipiscing elit, sed do eiusmod tempor incididunt ut labore et dolore magna aliqua. Quis ipsum suspendisse ultrices gravida. Risus commodo viverra maecenas accumsan lacus vel facilisis.</p>

<div class="abs acc" style="top:2166px">
  <span class="dash"></span><span class="q" style="color:var(--brand)">How to Invest?</span>
  <svg class="chev" width="12" height="8"><path d="M1 7l5-5 5 5" stroke="var(--brand)" fill="none" stroke-width="1.4"/></svg>
</div>
<p class="abs acc-body">Lorem ipsum dolor sit amet, consectetur adipiscing elit, sed do eiusmod tempor incididunt ut labore et dolore magna aliqua. Quis ipsum suspendisse ultrices gravida. Risus commodo viverra maecenas accumsan lacus vel facilisis.</p>
<div class="abs acc" style="top:2290px">
  <span class="dash" style="background:#222"></span><span class="q">How to Buy a House ?</span>
  <svg class="chev" width="12" height="8"><path d="M1 1l5 5 5-5" stroke="#999" fill="none" stroke-width="1.4"/></svg>
</div>
<div class="abs acc" style="top:2321px">
  <span class="dash" style="background:#222"></span><span class="q">How to Buy a House ?</span>
  <svg class="chev" width="12" height="8"><path d="M1 1l5 5 5-5" stroke="#999" fill="none" stroke-width="1.4"/></svg>
</div>
<div class="abs office" role="img" aria-label="Agent reviewing floor plans on a laptop beside an open planner"></div>

<!-- pricing -->
<section class="abs pricing"></section>
<h2 class="abs pricing-title">Save With Our Pricing Packages</h2>

<div class="abs plan" style="left:213px">
  <div class="head"><span class="tier">BASIC</span><span class="rate">$ 5.99 / <small>month</small></span></div>
  <ul><li><b>2 x</b> option 1</li><li><b>Free</b> option 2</li><li><b>Unlimited</b> option 3</li><li><b>Unlimited</b> option 4</li><li><b>Free</b> option 5</li></ul>
  <a class="sub">Subscribe</a>
</div>
<div class="abs plan dark" style="left:487px">
  <div class="head"><span class="tier">STANDARD</span><span class="rate">$ 5.99 / <small>month</small></span></div>
  <ul><li><b>2 x</b> option 1</li><li><b>Free</b> option 2</li><li><b>Unlimited</b> option 3</li><li><b>Unlimited</b> option 4</li><li><b>Free</b> option 5</li></ul>
  <a class="sub">Subscribe</a>
</div>
<div class="abs plan" style="left:760px">
  <div class="head"><span class="tier">PRO</span><span class="rate">$ 5.99 / <small>month</small></span></div>
  <ul><li><b>2 x</b> option 1</li><li><b>Free</b> option 2</li><li><b>Unlimited</b> option 3</li><li><b>Unlimited</b> option 4</li><li><b>Free</b> option 5</li></ul>
  <a class="sub">Subscribe</a>
</div>

<!-- footer -->
<footer class="abs footer" role="img" aria-label="City skyline under a purple overlay"></footer>
<div class="abs" style="left:156px;top:2983px;display:flex;align-items:center;gap:14px;color:#fff">
  <span style="width:36px;height:36px;border:2px solid #fff"></span>
  <span style="font-size:16px">KEYSTONE YIELD</span>
</div>
<p class="abs foot-copy">Lorem ipsum dolor sit amet, consectetur adipiscing elit, sed do eiusmod tempor incididunt ut labore et dolore magna aliqua. Quis ipsum suspendisse</p>

<h5 class="abs foot-head" style="left:468px">Links</h5>
<div class="abs flink" style="left:467px;top:3032px;line-height:22px">Home<br>About<br>What We Do</div>
<div class="abs flink" style="left:554px;top:3032px;line-height:22px">Pricing<br>Listing<br>Contact</div>

<h5 class="abs foot-head" style="left:693px">Information</h5>
<div class="abs flink" style="left:696px;top:3037px;display:flex;align-items:center;gap:10px">
  <svg width="13" height="13" viewBox="0 0 24 24" fill="none" stroke="#fff" stroke-width="1.6"><path d="M5 3h4l2 5-2.5 1.5a11 11 0 0 0 6 6L16 13l5 2v4a2 2 0 0 1-2 2A17 17 0 0 1 3 5a2 2 0 0 1 2-2z"/></svg>555-0193</div>
<div class="abs flink" style="left:696px;top:3067px;display:flex;align-items:center;gap:10px">
  <svg width="14" height="12" viewBox="0 0 24 20" fill="none" stroke="#fff" stroke-width="1.6"><rect x="2" y="6" width="20" height="13"/><path d="M2 6l10 7 10-7M6 6V2h12v4"/></svg>desk@kyield.co</div>
<div class="abs flink" style="left:697px;top:3095px;display:flex;align-items:center;gap:11px">
  <svg width="10" height="13" viewBox="0 0 9 12"><path d="M4.5.5A4 4 0 0 0 .5 4.5C.5 8 4.5 11.5 4.5 11.5S8.5 8 8.5 4.5a4 4 0 0 0-4-4z" fill="none" stroke="#fff"/><circle cx="4.5" cy="4.5" r="1.4" fill="#fff"/></svg>Location,Adress</div>

<h5 class="abs foot-head" style="left:876px">Get In Touch</h5>
<span class="abs social" style="left:880px"></span>
<span class="abs social" style="left:910px"></span>
<span class="abs social" style="left:940px"></span>
<span class="abs social" style="left:970px"></span>

<div class="abs copy">© 2019 Keystone Yield . All right reserved</div>

</body>
</html>
```